lunch and dinne(al a carte) menus

we are a medium sized licenced club that has taken back the dining in the club
in the western suburbs of sydney working class with a rugby league base
our logo is a wolf kelford hawks

Reason: We have changed the name to Bluegate grill it could be done as Bluegate or Bluegate or Bluegate We need a lunch menu and a seperate dinner menu eg Bluegate grill l u n c h or Bluegate grill d i n n e r

Reason: Weve changed the name

Target Market(s)

young families, working class rugby leagues sporty types

Industry/Entity Type

Club

Requirements
Must have
• user friendly

```html
<!DOCTYPE html>
<html lang="en">
<head>
<meta charset="utf-8">
<title>Bluegate Grill – Dinner Menu</title>
<link href="https://fonts.googleapis.com/css2?family=Alfa+Slab+One&family=Alegreya:wght@700;800;900&display=swap" rel="stylesheet">
<style>
  :root {
    --wood-dark: #3b2a12;
    --wood-mid: #4a3417;
    --band-dark: #4a2c18;
    --band-light: #6b4428;
    --paper-light: #ecc89a;
    --paper-mid: #e2b580;
    --paper-dark: #cf9a63;
    --ink: #5a2a14;
    --ink-heading: #7a4526;
    --ink-muted: #8a4a22;
    --leader: #8c6a48;
    --cream: #e9dccb;
    --white: #ffffff;
  }
  * { margin: 0; padding: 0; box-sizing: border-box; }
  html, body { width: 849px; height: 1200px; overflow: hidden; background: var(--wood-dark); }
  .menu {
    position: relative; width: 849px; height: 1200px; overflow: hidden;
    background: linear-gradient(90deg, var(--wood-dark), var(--wood-mid) 50%, var(--wood-dark));
    font-family: "Alegreya", Georgia, serif; color: var(--ink);
  }
  .wood-band { position: absolute; left: 0; width: 849px;
    background: linear-gradient(180deg, var(--band-light), var(--band-dark)); }
  .wood-band.top { top: 0; height: 156px; box-shadow: 0 6px 14px rgba(0,0,0,.55); z-index: 2; }
  .wood-band.bottom { top: 1110px; height: 90px; border-top: 2px solid #7a5234; box-shadow: 0 -4px 12px rgba(0,0,0,.5); z-index: 2; }
  .brand {
    position: absolute; top: 22px; left: 0; width: 100%; text-align: center;
    font-family: "Alfa Slab One", Georgia, serif; font-size: 54px; line-height: 1;
    color: var(--cream); letter-spacing: 1px; text-transform: uppercase;
  }
  .service {
    position: absolute; top: 92px; left: 0; width: 100%; text-align: center;
    font-family: "Alfa Slab One", Georgia, serif; font-size: 40px; line-height: 1;
    color: var(--white); letter-spacing: 1px;
  }
  .footer-note {
    position: absolute; top: 1144px; left: 0; width: 100%; text-align: center;
    font-family: "Alfa Slab One", Georgia, serif; font-size: 14.5px;
    color: var(--cream); letter-spacing: .2px; z-index: 3;
  }
  .parchment {
    position: absolute; left: 84px; top: 150px; width: 683px; height: 962px;
    background: radial-gradient(ellipse at 45% 40%, var(--paper-light), var(--paper-mid) 60%, var(--paper-dark));
    box-shadow: 0 0 22px rgba(0,0,0,.6);
  }
  .section-title {
    position: absolute; left: 137px; font-weight: 900; color: var(--ink-heading);
    font-size: 35px; line-height: 1; letter-spacing: .5px;
  }
  .rule { position: absolute; left: 137px; width: 561px; border-top: 1.5px dashed var(--leader); }
  .col-head { position: absolute; top: 188px; font-weight: 800; font-size: 15px; color: var(--ink); }
  .row {
    position: absolute; left: 138px; width: 533px; display: flex; align-items: baseline;
    font-weight: 900; font-size: 14.5px; line-height: 1; text-transform: uppercase; color: var(--ink);
  }
  .row .dots { flex: 1; border-bottom: 1px dashed var(--leader); margin: 0 6px; transform: translateY(-2px); }
  .row .member { width: 42px; text-align: center; }
  .row .dots.short { flex: 0 0 42px; margin: 0 4px; }
  .row .visitor { width: 28px; text-align: right; }
  .row .qty { font-size: 12px; }
  .note { position: absolute; left: 138px; font-weight: 800; font-size: 12.5px; color: var(--ink-muted); }
</style>
</head>
<body>
<main class="menu">
  <header class="wood-band top">
    <h1 class="brand">Bluegate Grill</h1>
    <p class="service">DINNER</p>
  </header>

  <section class="parchment" aria-hidden="false"></section>

  <h2 class="section-title" style="top:176px;font-size:31px;letter-spacing:2px;">????????</h2>
  <span class="col-head" style="left:545px;">Member</span>
  <span class="col-head" style="left:635px;">Visitor</span>
  <div class="rule" style="top:219px;"></div>

  <div class="row" style="top:232px;"><span>Dampers</span><span class="dots"></span><span class="member">$7</span><span class="dots short"></span><span class="visitor">$7</span></div>
  <div class="row" style="top:263px;"><span>Garlic Damper</span><span class="dots"></span><span class="member">$7</span><span class="dots short"></span><span class="visitor">$7</span></div>
  <div class="row" style="top:293px;"><span>Herb Damper</span><span class="dots"></span><span class="member">$7</span><span class="dots short"></span><span class="visitor">$7</span></div>
  <div class="row" style="top:323px;"><span>Bruschetta</span><span class="dots"></span><span class="member">$9</span><span class="dots short"></span><span class="visitor">$9</span></div>

  <h2 class="section-title" style="top:360px;">LIGHT MEALS</h2>
  <div class="rule" style="top:401px;"></div>

  <div class="row" style="top:416px;"><span>Chips</span><span class="dots"></span><span class="member">$6</span><span class="dots short"></span><span class="visitor">$6</span></div>
  <div class="row" style="top:446px;"><span>Wedges</span><span class="dots"></span><span class="member">$6</span><span class="dots short"></span><span class="visitor">$6</span></div>
  <p class="note" style="top:466px;">With sour cream &amp; sweet chilli</p>
  <div class="row" style="top:497px;"><span>Bowl of Salad</span><span class="dots"></span><span class="member">$6</span><span class="dots short"></span><span class="visitor">$6</span></div>
  <div class="row" style="top:528px;"><span>Bowl of Steamed Vegetables</span><span class="dots"></span><span class="member">$6</span><span class="dots short"></span><span class="visitor">$6</span></div>
  <div class="row" style="top:558px;"><span>Tempura Crumbed Clamari</span><span class="dots"></span><span class="member">$8</span><span class="dots short"></span><span class="visitor">$10</span></div>
  <p class="note" style="top:578px;">Served with salad</p>
  <div class="row" style="top:608px;"><span>Battered Flathead Fillets</span><span class="dots"></span><span class="member">$8</span><span class="dots short"></span><span class="visitor">$10</span></div>
  <p class="note" style="top:628px;">Served with salad</p>
  <div class="row" style="top:659px;"><span>Whiting Fillets</span><span class="dots"></span><span class="member">$8</span><span class="dots short"></span><span class="visitor">$10</span></div>
  <p class="note" style="top:679px;">Served with salad</p>
  <div class="row" style="top:709px;"><span>Prawn Salad</span><span class="dots"></span><span class="member">$10</span><span class="dots short"></span><span class="visitor">$12</span></div>
  <div class="row" style="top:740px;"><span>Garlic or Chilli Prawns</span><span class="dots"></span><span class="member">$8</span><span class="dots short"></span><span class="visitor">$10</span></div>
  <p class="note" style="top:760px;">Served with rice &amp; salad</p>
  <div class="row" style="top:790px;"><span>Satay Chicken Kebabs</span><span class="dots"></span><span class="member">$8</span><span class="dots short"></span><span class="visitor">$10</span></div>
  <p class="note" style="top:810px;">Served with rice &amp; salad</p>
  <div class="row" style="top:841px;"><span>Baked Potato</span><span class="dots"></span><span class="member">$10</span><span class="dots short"></span><span class="visitor">$12</span></div>
  <p class="note" style="top:860px;">With bolognese sauce &amp; melted cheese with sour cream</p>
  <div class="row" style="top:891px;"><span>Nachos</span><span class="dots"></span><span class="member">$10</span><span class="dots short"></span><span class="visitor">$12</span></div>

  <h2 class="section-title" style="top:926px;">SYDNEY ROCK OYSTERS</h2>
  <div class="rule" style="top:964px;"></div>

  <div class="row" style="top:983px;"><span>Kilpatrick • Natural • Mornay</span><span class="dots"></span><span class="qty">Dozen</span><span class="dots" style="flex:0 0 14px;margin:0 3px;"></span><span class="member" style="width:28px;">$22</span><span class="dots short"></span><span class="visitor">$24</span></div>
  <div class="row" style="top:1012px;"><span style="flex:1"></span><span class="qty">1/2 Dozen</span><span class="dots" style="flex:0 0 14px;margin:0 3px;"></span><span class="member" style="width:28px;">$12</span><span class="dots short"></span><span class="visitor">$14</span></div>

  <footer class="wood-band bottom"></footer>
  <p class="footer-note">ALL MAIN MEALS ARE SERVED WITH CHIPS &amp; SALAD OR MASHED POTATO &amp; VEGETABLES</p>
</main>
</body>
</html>
```